Marlow Summit Holdings, LLC

I need a new business card desperately.

Please update my business card. I am looking for a professional modern classy design like the Brightfen Partners card in the attachments.

Industry/Entity Type

Investment

Contact Information for Business Card

Colors

Designer to choose colors to be used in the design.

```html
<!DOCTYPE html>
<html lang="en">
<head>
<meta charset="utf-8">
<title>Marlow Summit Holdings — Business Card</title>
<link rel="stylesheet" href="https://fonts.googleapis.com/css2?family=Nunito+Sans:wght@400;600;700&display=swap">
<style>
  :root {
    --stage: #0f3840;
    --teal-deep: #0b5b65;
    --teal-soft: #12727c;
    --white: #ffffff;
    --ink-grey: #6e6e6e;
    --ink-dark: #505357;
    --font-text: "Nunito Sans", sans-serif;
  }
  * { box-sizing: border-box; margin: 0; padding: 0; }
  html, body {
    width: 1200px; height: 1200px; overflow: hidden;
    background: var(--stage);
    font-family: var(--font-text);
  }
  .stage { position: relative; width: 1200px; height: 1200px; }

  .card {
    position: absolute; left: 234px; width: 732px; height: 418px; overflow: hidden;
  }
  .card--front { top: 154px; background: var(--teal-deep); }
  .card--back  { top: 628px; background: var(--white); }

  .brand-square {
    position: absolute; width: 100px; height: 100px;
  }
  .card--front .brand-square { left: 228px; top: 158px; background: var(--white); }
  .card--back  .brand-square { left: 228px; top: 151px; background: var(--teal-deep); }

  .wordmark {
    position: absolute; left: 333px;
    font-family: var(--font-text); font-weight: 400;
    font-size: 32px; line-height: 28.5px; letter-spacing: 0.2em;
    text-transform: uppercase;
  }
  .card--front .wordmark { top: 165px; color: var(--white); }
  .card--back  .wordmark { top: 157px; color: var(--ink-grey); }
  .wordmark span { display: block; }

  .holder { position: absolute; left: 38px; top: 32px; }
  .holder__name {
    font-weight: 700; font-size: 27px; line-height: 30px;
    color: var(--teal-deep); letter-spacing: 0.01em;
  }
  .holder__title {
    font-weight: 400; font-size: 14.5px; line-height: 16px;
    color: var(--ink-dark); text-transform: uppercase;
  }

  .contact {
    position: absolute; font-size: 15px; font-weight: 600;
    color: var(--ink-dark); text-transform: uppercase; line-height: 21px;
  }
  .contact svg { position: absolute; fill: var(--teal-deep); }
  .contact--address { left: 61px; top: 326px; }
  .contact--address svg { left: -22px; top: 2px; width: 20px; height: 26px; }
  .contact--email { left: 61px; top: 374px; }
  .contact--email svg { left: -23px; top: 3px; width: 22px; height: 16px; }
  .contact--phone { left: 545px; top: 372px; }
  .contact--phone svg { left: -21px; top: -1px; width: 14px; height: 24px; }
</style>
</head>
<body>
<main class="stage">

  <section class="card card--front" aria-label="Card front">
    <div class="brand-square"></div>
    <h1 class="wordmark"><span>Marlow</span><span>Summit</span><span>Holdings</span></h1>
  </section>

  <section class="card card--back" aria-label="Card back">
    <div class="holder">
      <p class="holder__name">OWEN R. MARLOW</p>
      <p class="holder__title">Managing Partner</p>
    </div>

    <div class="brand-square"></div>
    <p class="wordmark"><span>Marlow</span><span>Summit</span><span>Holdings</span></p>

    <p class="contact contact--address">
      <svg viewBox="0 0 20 26" aria-hidden="true">
        <path d="M10 1a7 7 0 0 0-7 7c0 5 7 12 7 12s7-7 7-12a7 7 0 0 0-7-7zm0 9.5a2.6 2.6 0 1 1 0-5.2 2.6 2.6 0 0 1 0 5.2z"/>
        <path d="M1 25l3-6h2.5l-.8 1.4H5L3.3 23.6h13.4L15 20.4h-.7l-.8-1.4H16l3 6z"/>
      </svg>
      4820 Cedar Hollow Road<br>Austin, TX 78731
    </p>

    <p class="contact contact--email">
      <svg viewBox="0 0 22 16" aria-hidden="true">
        <path d="M0 0h22v16H0zM2 2.2v11.6l5.6-5.8zm18 0l-5.6 5.8L20 13.8zM2.6 1.5L11 9.7l8.4-8.2zM8.6 9L2.8 14.5h16.4L13.4 9 11 11.3z"/>
      </svg>
      omarlow@marlowsummit.com
    </p>

    <p class="contact contact--phone">
      <svg viewBox="0 0 14 24" aria-hidden="true">
        <path d="M2.5 0h9A2.5 2.5 0 0 1 14 2.5v19a2.5 2.5 0 0 1-2.5 2.5h-9A2.5 2.5 0 0 1 0 21.5v-19A2.5 2.5 0 0 1 2.5 0zM2 3v16h10V3zm5 17.2a1.3 1.3 0 1 0 0 2.6 1.3 1.3 0 0 0 0-2.6z"/>
      </svg>
      512.555.0148 Direct
    </p>
  </section>

</main>
</body>
</html>
```